Landing Page IT Security Vendor

We need a landing page that uses our colour scheme (www.veldonguard.com). We created a draft (see attached). We do not need standard stock template design pages. Please only apply if you can design pages from scratch and try to be as close as possible to our draft. It is ok to also purchase commecrial stock pictures

Coding

Coded - Design and coding required

Number of Pages Required

1 page

```html
<!DOCTYPE html>
<html lang="en">
<head>
<meta charset="utf-8">
<title>Veldon Security – Security Awareness Training</title>
<link href="https://fonts.googleapis.com/css2?family=Montserrat:wght@500;600;700&family=Roboto:wght@400;500&display=swap" rel="stylesheet">
<style>
:root{
  --teal:#1fbfc6;
  --teal-dark:#139ea5;
  --teal-btn:#2aa9b4;
  --orange:#f98a0c;
  --orange-light:#fba619;
  --ink:#333333;
  --body:#444444;
  --muted:#555555;
  --bg:#f7f7f7;
  --white:#ffffff;
  --grey-band:#6b6b6b;
}
*{margin:0;padding:0;box-sizing:border-box}
html,body{width:1200px;height:2251px;overflow:hidden}
body{position:relative;background:var(--bg);font-family:"Roboto",sans-serif;color:var(--body)}
.abs{position:absolute}
.btn{position:absolute;display:flex;align-items:center;justify-content:center;color:var(--white);font-family:"Roboto",sans-serif;font-size:15px;background:linear-gradient(180deg,var(--orange-light),var(--orange));border-radius:2px}
.btn.teal{background:var(--teal-btn)}
/* hero */
.hero{left:0;top:0;width:1200px;height:520px;background:var(--teal);overflow:hidden}
.hero-photo{left:0;top:0;width:1200px;height:520px;background:radial-gradient(ellipse at 30% 50%,rgba(10,110,118,.45),transparent 60%),radial-gradient(ellipse at 75% 40%,rgba(10,110,118,.35),transparent 55%),var(--teal)}
.brand{font-family:"Montserrat",sans-serif;font-weight:700;color:var(--ink);display:flex;align-items:center;gap:8px}
.brand .dot{width:26px;height:26px;background:var(--orange);border-radius:50%}
.hero .brand{left:56px;top:44px;font-size:26px}
.award{top:48px;display:flex;gap:10px;align-items:center;color:var(--white);font-size:10.5px;line-height:14px;font-family:"Montserrat",sans-serif;font-weight:500}
.award svg{flex:none}
.hero-kicker{left:0;width:1200px;top:198px;text-align:center;color:var(--white);font-family:"Montserrat",sans-serif;font-weight:700;font-size:27px;letter-spacing:1.5px}
.hero-title{left:0;width:1200px;top:234px;text-align:center;color:var(--white);font-family:"Montserrat",sans-serif;font-weight:500;font-size:35px;line-height:47px}
/* help */
.section-title{left:0;width:1200px;text-align:center;color:var(--ink);font-family:"Montserrat",sans-serif;font-weight:600}
.card{top:692px;width:320px;height:358px;background:var(--white)}
.card-icon{top:646px;width:92px;height:92px;border-radius:50%;background:var(--white);box-shadow:0 0 10px rgba(0,0,0,.06);display:flex;align-items:center;justify-content:center}
.card h3{position:absolute;left:24px;top:60px;width:280px;color:var(--orange);font-family:"Montserrat",sans-serif;font-weight:500;font-size:15px;line-height:18px;text-transform:uppercase}
.card .lead{position:absolute;left:24px;width:275px;color:var(--ink);font-size:13.5px;line-height:18px;font-weight:500}
.card .desc{position:absolute;left:24px;width:275px;color:var(--muted);font-size:12px;line-height:18px}
.card .btn{left:23px;top:298px;width:272px;height:32px}
/* mssp */
.mssp{left:0;top:1116px;width:1200px;height:120px;background:var(--teal);overflow:hidden}
.mssp h2{position:absolute;left:206px;top:42px;color:var(--white);font-family:"Montserrat",sans-serif;font-weight:500;font-size:29px;letter-spacing:.5px}
/* trust */
.trust p{left:0;width:1200px;text-align:center;font-size:12px;line-height:18px;color:var(--muted)}
.logo-cell{display:flex;align-items:center;justify-content:center;width:205px;height:112px;border-right:1px solid #ececec;font-family:"Roboto",sans-serif;font-weight:500;font-size:22px;color:var(--ink);gap:8px}
.logo-cell .sq{width:22px;height:22px;background:var(--teal)}
/* footer */
.footer{left:0;top:1852px;width:1200px;height:399px;background:var(--teal);color:var(--white)}
.footer h4{position:absolute;top:56px;font-family:"Montserrat",sans-serif;font-weight:500;font-size:16px}
.footer .txt{position:absolute;font-size:12.5px;line-height:19px}
.phones{display:grid;grid-template-columns:88px auto}
.badge{position:absolute;top:2150px;width:72px;height:72px}
</style>
</head>
<body>

<section class="abs hero">
  <div class="abs hero-photo" role="img" aria-label="Team of colleagues working together at computers, tinted teal"></div>
  <div class="abs brand"><span class="dot"></span>Veldon</div>

  <div class="abs award" style="left:268px">
    <svg width="24" height="24" viewBox="0 0 24 24" fill="none" stroke="#fff" stroke-width="2"><path d="M7 3h10v5a5 5 0 0 1-10 0z"/><path d="M7 5H3a4 4 0 0 0 4 4M17 5h4a4 4 0 0 1-4 4M12 13v5M8 21h8"/></svg>
    <span>In 2020, VELDON won the Digital Defense<br>Excellence Award for Best "Anti Phishing</span>
  </div>
  <div class="abs award" style="left:542px">
    <svg width="26" height="26" viewBox="0 0 26 26" fill="none" stroke="#fff" stroke-width="2"><circle cx="13" cy="13" r="10" stroke-dasharray="3 2"/><path d="M13 8l1.6 3.3 3.6.5-2.6 2.5.6 3.6-3.2-1.7-3.2 1.7.6-3.6-2.6-2.5 3.6-.5z" fill="#fff"/></svg>
    <span>In 2020, VELDON won the Digital Defense Excellence<br>Award for Best "Security Education Platform</span>
  </div>
  <div class="abs award" style="left:864px">
    <svg width="26" height="26" viewBox="0 0 26 26" fill="none" stroke="#fff" stroke-width="2"><circle cx="13" cy="13" r="10" stroke-dasharray="3 2"/><path d="M11 9l3-1v10"/></svg>
    <span>2020 Gold Winner "Cyber Security Education<br>and Training In the SecureTech Product guide</span>
  </div>

  <div class="abs hero-kicker">CYBER SECURITY STARTS WITH PEOPLE</div>
  <div class="abs hero-title">Train your staff with veldon and improve cyber<br>security awareness</div>
  <div class="btn" style="left:524px;top:348px;width:152px;height:32px">Request a demo</div>
</section>

<section class="help">
  <h2 class="abs section-title" style="top:576px;font-size:29px">How Can We Help?</h2>

  <article class="abs card" style="left:89px">
    <h3>Import our training courses<br>in your LMS</h3>
    <p class="lead" style="top:112px">Buy out of the box or custom tailored security courses you can import in your elearning (SCORM)</p>
    <p class="desc" style="top:184px">VELDON offers 250 fully customizable training modules in +30 languages. Games, videos, exams, posters, offline, micro-training and much more!</p>
    <div class="btn">Explore our training</div>
  </article>
  <div class="abs card-icon" style="left:202px">
    <svg width="50" height="50" viewBox="0 0 50 50" fill="none" stroke="var(--teal)" stroke-width="2"><rect x="18" y="6" width="26" height="18"/><path d="M24 20v-5M30 20v-9M36 20v-6" stroke="var(--orange)"/><circle cx="12" cy="20" r="4"/><path d="M6 38v-8a6 6 0 0 1 12 0v8"/><circle cx="28" cy="33" r="3"/><circle cx="40" cy="33" r="3"/><path d="M23 44a5 5 0 0 1 10 0M35 44a5 5 0 0 1 10 0"/></svg>
  </div>

  <article class="abs card" style="left:440px">
    <h3>Let us develop a security<br>awareness&nbsp; program</h3>
    <p class="lead" style="top:112px">VELDON Security will assist you in improving security awareness - with money back guarantee!</p>
    <p class="desc" style="top:184px">Our security awareness specialists will identify risky users via phishing simulations. We develop a tailored awareness program and reduce your exposure to social hacking.</p>
    <div class="btn teal">Explore our services</div>
  </article>
  <div class="abs card-icon" style="left:554px">
    <svg width="56" height="46" viewBox="0 0 56 46" fill="none" stroke="var(--teal)" stroke-width="2"><rect x="3" y="4" width="50" height="38" rx="2"/><path d="M3 12h50"/><path d="M15 22l-5 5 5 5M25 22l5 10M20 20l-3 14" stroke="var(--orange)"/><path d="M36 20h12M36 27h12M36 34h12"/></svg>
  </div>

  <article class="abs card" style="left:793px">
    <h3>Install the veldon software<br>on-premise or get access to<br>the SaaS version</h3>
    <p class="lead" style="top:130px">You want to run the campaign yourself? Choose your prefered setup type and get started in 24h!</p>
    <p class="desc" style="top:202px">The VELDON software can be installed on-premise or in the cloud. If you don't want to deal with the installation we onboard you in 24 h on our SaaS!</p>
    <div class="btn">Explore our software</div>
  </article>
  <div class="abs card-icon" style="left:906px">
    <svg width="54" height="50" viewBox="0 0 54 50" fill="none" stroke="var(--teal)" stroke-width="2"><rect x="4" y="14" width="38" height="26"/><path d="M18 46h10M23 40v6"/><circle cx="16" cy="26" r="4" stroke="var(--orange)"/><circle cx="40" cy="12" r="6" stroke="var(--orange)"/><path d="M40 2v4M40 18v4M30 12h4M46 12h4"/></svg>
  </div>
</section>

<section class="abs mssp">
  <svg class="abs" style="left:0;top:0" width="1200" height="120"><polygon points="968,0 1200,0 1200,120 889,120" fill="var(--grey-band)"/></svg>
  <h2>Veldon is also available for MSSP</h2>
  <div class="btn" style="left:865px;top:44px;width:126px;height:31px">Learn more</div>
</section>

<section class="trust">
  <h2 class="abs section-title" style="top:1306px;font-size:31px;line-height:39px">Already over 12'000'000 employees worldwide<br>trust and use VELDON.</h2>
  <p class="abs" style="top:1398px">Veldon Security is a name you can trust! Because we have won countless awards since 2015 and help well-known<br>brands around the world. You know you're getting a quality solution with us.</p>
  <p class="abs" style="top:1446px">Our services can be customized to fit your needs and company size. Talk to our team today to learn more.</p>
  <div class="btn" style="left:440px;top:1491px;width:320px;height:31px">Get in contact with the veldon team now!</div>

  <div class="abs" style="left:89px;top:1563px;display:flex;border-bottom:1px solid #ececec">
    <div class="logo-cell"><span class="sq"></span>Norvana</div>
    <div class="logo-cell">Railtrek</div>
    <div class="logo-cell">Hausmont</div>
    <div class="logo-cell">Kellerman</div>
    <div class="logo-cell" style="border-right:none">Altiroute</div>
  </div>
  <div class="abs" style="left:191px;top:1675px;display:flex">
    <div class="logo-cell">Grainwell</div>
    <div class="logo-cell">Vantor Informatik</div>
    <div class="logo-cell">Chemvista</div>
    <div class="logo-cell" style="border-right:none"><span class="sq" style="background:var(--orange)"></span>Cityclean</div>
  </div>
</section>

<footer class="abs footer">
  <div class="abs brand" style="left:98px;top:54px;font-size:30px"><span class="dot"></span>Veldon</div>
  <div class="txt" style="left:98px;top:106px;font-size:11.5px">All Rights Reserved 2020</div>

  <h4 style="left:352px">ADDRESS</h4>
  <div class="txt" style="left:352px;top:94px">EUROPE VELDON SECURITY<br>AG Lindenweg 18 I 6301<br>Zug I Switzerland<br><br>NORTH AMERICA VELDON SECURITY<br>USA 4820 Harbor Loop Suite 210<br>Austin, TX 78701</div>

  <h4 style="left:616px">PHONE</h4>
  <div class="txt phones" style="left:616px;top:94px">
    <span>Global:</span><span>+41 44 000 12 34</span>
    <span>USA:</span><span>+1-512-555-0142</span>
    <span>USA Support:</span><span>+1-512-555-0178</span>
    <span>France:</span><span>+33 600 000 123</span>
    <span>UK:</span><span>+44 (0) 7700 900123</span>
  </div>

  <h4 style="left:879px">LANGUAGE</h4>
  <div class="txt" style="left:879px;top:92px">English &nbsp;⌄</div>

  <div class="abs" style="left:89px;top:263px;width:1023px;height:1px;background:rgba(255,255,255,.35)"></div>
</footer>

<svg class="abs" style="left:0;top:0;pointer-events:none" width="1200" height="2251" aria-label="Award and certification badges">
  <g fill="rgba(255,255,255,.9)">
    <rect x="90" y="2150" width="70" height="68" rx="4"/>
    <circle cx="216" cy="2184" r="34"/>
    <rect x="294" y="2148" width="52" height="72" rx="3"/>
    <rect x="390" y="2150" width="56" height="70"/>
    <rect x="488" y="2150" width="56" height="70"/>
    <rect x="586" y="2150" width="50" height="70"/>
    <rect x="680" y="2160" width="90" height="46" rx="6"/>
    <rect x="814" y="2156" width="56" height="58" rx="4"/>
    <rect x="916" y="2162" width="104" height="42" rx="21"/>
    <circle cx="1084" cy="2184" r="27"/>
  </g>
</svg>

</body>
</html>
```